Opening new doors for every person - Solvane-Ridge

Please note that whoever will win this project , a 1on1 Powerpoint design project will separately be launched and will be offered to the winning designer.

---------
This letterhead is to provide proposals, as well as manuals for my clients.

I am looking for the letter, power point design and business card that inspires people when they see it, that they feel that design has been done with love and passion. Something that is professional, simple and yet creative, Business like, yet spiritual. That inspires growth!

This part of the branding for my company, therefore the business card as well as the power point design that will come after as 1on1 project should have the same team and feeling.

Solvane ridge, The company will be providing Coaching services (one-one or groups) to corporations, teams and individuals, partnering with them to achieve their goals/vision, by helping them to remove the self-imposed limiting beliefs, helping them to get them out of their own way, helping them to raise their level of consciousness and self-awareness.

The vision is: Bring conscious leadership to the workplace and to individuals for the wellbeing of humanity.

I know that somewhere out there will resonate with this, and will be inspired to provide the best design :) thank you very much!!!!!

MPORTANT:
- To use Free Fonts - let me know where I can download them
- Editable formats please for the double sized business card

LOGO is attached in pdf. If needed other file type please let me know

Thank you thank you in advance for your time and inspiration!! Sending good vibes for a great design out there

Must Have:
- Please keep on mind that the cards - power point will have the same feeling - Corporate branding
- that is not to heavy to look at it, that is simple and beautiful and inspiring
- Looking to have Calibri or Calibri light font

imple, yet inspirational - Professional, yet playful - business like, yet spiritual

I am looking for something different that the "standard" designs out there.

For example, the Logo of the company in the back side with a quote and the front side something simple, yet inspiring. that has the contact info as well as the social media details LinkedIn - Facebook - tweeter - website

Open for suggestions and inspiration :)

Thank you!

• - Please keep on mind that the cards - power point will have the same feeling
• - Corporate branding
• - that is not to heavy to look at it, that is simple and beautiful and inspiring
• - Looking to have Calibri or Calibri light font
• - Corporate colours as the logo

```html
<!DOCTYPE html>
<html lang="en">
<head>
<meta charset="utf-8">
<title>Solvane-Ridge Business Card</title>
<link rel="stylesheet" href="https://fonts.googleapis.com/css2?family=Carlito:wght@400;700&display=swap">
<style>
  :root {
    --brand-blue: #184f8c;
    --brand-yellow: #fbbd18;
    --card-white: #ffffff;
    --backdrop: #eeebe7;
    --text-light: #ffffff;
  }
  * { box-sizing: border-box; margin: 0; padding: 0; }
  html, body {
    width: 1200px; height: 900px; overflow: hidden;
    background: var(--backdrop);
  }
  .canvas {
    position: relative; width: 1200px; height: 900px;
    font-family: "Carlito", "Calibri", sans-serif;
  }

  .card { position: absolute; overflow: hidden; box-shadow: 0 4px 14px rgba(0,0,0,0.12); }

  /* Front: contact side */
  .card-front {
    left: 78px; top: 34px; width: 588px; height: 363px;
    background: var(--brand-blue);
    color: var(--text-light);
  }
  .front-emblem {
    position: absolute; left: 305px; top: 20px;
    width: 330px; height: 330px; border-radius: 50%;
    background: var(--brand-yellow);
    display: flex; align-items: center; justify-content: center;
  }
  .front-emblem .brand-name {
    font-weight: 700; font-size: 30px; color: var(--brand-blue);
    margin-right: 40px;
  }
  .holder { position: absolute; left: 38px; top: 56px; }
  .holder-name { font-size: 22px; font-weight: 700; letter-spacing: 0.3px; line-height: 1.1; }
  .holder-role { font-size: 16px; line-height: 1.1; }
  .contact-list { position: absolute; left: 40px; top: 186px; list-style: none; font-size: 16px; }
  .contact-list li { display: flex; align-items: center; height: 21.7px; }
  .contact-list svg { width: 12px; height: 12px; margin-right: 11px; fill: var(--text-light); }
  .address { position: absolute; left: 38px; top: 281px; font-size: 16px; line-height: 22px; font-style: normal; }

  /* Back: brand side */
  .card-back {
    left: 388px; top: 505px; width: 567px; height: 352px;
    background: var(--card-white);
    display: flex; align-items: center; justify-content: center; gap: 28px;
  }
  .back-mark {
    width: 100px; height: 100px; border-radius: 50%;
    background: var(--brand-blue);
    flex: none;
  }
  .back-name {
    font-size: 34px; font-weight: 700; color: var(--brand-blue);
  }
</style>
</head>
<body>
<main class="canvas">
  <section class="card card-front" aria-label="Business card front">
    <div class="front-emblem"><span class="brand-name">Solvane-Ridge</span></div>
    <div class="holder">
      <p class="holder-name">MAREN HOLLOWAY</p>
      <p class="holder-role">Managing Director</p>
    </div>
    <ul class="contact-list">
      <li><svg viewBox="0 0 12 12"><path d="M1 4c0-2 2-3 5-3s5 1 5 3l-2 1-1-2H4L3 5zM2 6h8l1 5H1z"/></svg>(044)555014782</li>
      <li><svg viewBox="0 0 12 12"><path d="M3 0h6v3H3zM1 4h10v8H1zm2 2v1h2V6zm4 0v1h2V6zM3 9v1h2V9zm4 0v1h2V9z"/></svg>(044)555014783</li>
      <li><svg viewBox="0 0 12 12"><path d="M0 2h12v8H0zm1 1v.4l5 3.2 5-3.2V3z"/></svg>hello@solvaneridge.com</li>
      <li><svg viewBox="0 0 12 12"><path d="M6 0a6 6 0 1 0 0 12A6 6 0 0 0 6 0zm-1 2v2l-2 1 1 2 2 1v2L4 9 2 6l1-3zm3 1l2 2-1 3-2 1V7l1-1z"/></svg>www.solvaneridge.com</li>
    </ul>
    <address class="address">48, Harbour Lane West<br>Eastmere, 40218</address>
  </section>

  <section class="card card-back" aria-label="Business card back">
    <div class="back-mark"></div>
    <p class="back-name">Solvane-Ridge</p>
  </section>
</main>
</body>
</html>
```